The Meridale Works
Buy+Sell+Repair & Take trade-ins. New & Used, All makes and models
24 Hours or so left in this contest. We have seen many good designs and a few of you are in contention as you have incorporated what we sell like GPS & Total stations etc which we like. We hope to get some even stronger options with our suggestions in mind in the closing hours but also the sooner the better. If we like your design but would simply like to make a small revision, we would like to give you time to correct prior to us picking another winner. Thanks for all your efforts.
draft #155 We like your creativity! Would like to see some new drafts from you soon showing some of the suggestions mentioned in previous posts. Maybe make the large earth and satellite more translucent. Put dots in between words like buy+sell etc instread of plus signs. Use icons to show quorvel, bramnet, phone, email and Valto then follow with proper info. Move everything around if need be to try to make look clean while having this info available. Look forward to new options from you. Thanks
#162 please make Icons & info larger.
#163 Can you move our logo & company name up a little & put buy, sell ect. just under it in the grey area.
Then put " Dealing in VORANT, MELDRIX, KAPUNO, FELSTOW, & ZIRVAN." in the blue area.
Note Please use period or comma instead of "+" on designs.
Project# 102,
I really like this one. Will you :
1) Take away the "box" from our names & put Names in upper corner, & put "Phone# & Email & address."
2) Keep our logo & company name as is.
3) Bottom left area put " Buy. Sell. Trade. Repair. New & Used. GPS. Robotics. Total Stations. Theodolites. & Levels "
4) Bottom Right area put "Bramnet, Valto, Quorvel, ect." (Please use "Icon" instead of words.)
5)To every one .... I would like to see the package deal after we get the card layout handled. ( I also like some of the ideas of the "swoosh" on the cars but don't know if the "info" will fit rite.
Thank you for your help.
Also please no highlight block over our names
Fifth but very important is that we are primarily an Internet based company and our Address is not really needed on our business card. Addreess could be removed but please include a second email address being dana@themeridaleworks.example to this card.
Fourth, Please keep with the concept I have seen on several designs that puts a translucent version of our globe logo on the opposite side of the darker logo. This more translucent globe can have our company contact info written on top of it as long as it still looks clean and the info is very clear to read.
Third, We like a small swoosh to seperate the card into two halves.
Second I very much need the card to have the logo and our name but then under that it should read Buy+Sell+Repair+Trade-in+New & Used+ All makes and Models. as seen in design #152
This should be a must!
Greeting all,
Sorry that I have not given much feedback yet but things are very busy. I have looked over the designs and have a few suggestions. First I will probably choose a design that gives the whole stationary and envelope options too.

```html
<!DOCTYPE html>
<html lang="en">
<head>
<meta charset="utf-8">
<title>The Meridale Works — Business Card</title>
<link href="https://fonts.googleapis.com/css2?family=Roboto:wght@400;700&display=swap" rel="stylesheet">
<style>
  :root {
    --page: #e9e9ec;
    --card-white: #ffffff;
    --navy-deep: #05081a;
    --navy: #0d1a4a;
    --stripe-blue: #3d73d9;
    --stripe-dark: #1b2f6e;
    --brand-blue: #1f3f9a;
    --text-light: #ffffff;
    --text-soft: #dfe6f5;
    --rule: #8c9cc4;
    --icon-disc: #cfd8ec;
  }
  html, body {
    margin: 0;
    width: 1200px;
    height: 742px;
    overflow: hidden;
    background: var(--page);
    font-family: "Roboto", Arial, sans-serif;
  }
  .card {
    position: absolute;
    left: 40px;
    top: 40px;
    width: 1120px;
    height: 662px;
    border-radius: 34px;
    overflow: hidden;
    background: var(--card-white);
    box-shadow: 0 6px 18px rgba(0,0,0,0.18);
  }
  .card-art {
    position: absolute;
    inset: 0;
  }
  .brand {
    position: absolute;
    left: 250px;
    top: 206px;
    color: var(--brand-blue);
    font-weight: 700;
    line-height: 1;
  }
  .brand-lead {
    display: block;
    font-size: 30px;
    margin-bottom: 4px;
  }
  .brand-name {
    display: block;
    font-size: 58px;
    letter-spacing: 1px;
  }
  .tagline,
  .names {
    position: absolute;
    left: 0;
    width: 940px;
    margin: 0;
    text-align: center;
  }
  .tagline {
    top: 350px;
    color: var(--text-soft);
    font-size: 22px;
  }
  .names {
    top: 400px;
    color: var(--text-light);
    font-size: 36px;
    font-weight: 700;
  }
  .contact-row {
    position: absolute;
    left: 0;
    width: 940px;
    display: flex;
    justify-content: center;
    gap: 48px;
    color: var(--text-soft);
    font-size: 28px;
  }
  .contact-row.primary { top: 478px; }
  .contact-row.secondary { top: 588px; }
  .contact-item {
    display: flex;
    align-items: center;
    gap: 14px;
  }
  .contact-icon {
    width: 30px;
    height: 30px;
    flex: none;
  }
</style>
</head>
<body>
  <div class="card">
    <svg class="card-art" width="1120" height="662" viewBox="0 0 1120 662">
      <defs>
        <radialGradient id="darkPanel" cx="0.45" cy="0.2" r="0.75">
          <stop offset="0" stop-color="#6f95e8"/>
          <stop offset="0.25" stop-color="#2c52b0"/>
          <stop offset="0.6" stop-color="#0d1a4a"/>
          <stop offset="1" stop-color="#05081a"/>
        </radialGradient>
        <linearGradient id="satelliteTone" x1="0" y1="0" x2="1" y2="1">
          <stop offset="0" stop-color="#5a6a88"/>
          <stop offset="0.5" stop-color="#2a3858"/>
          <stop offset="1" stop-color="#0d1a4a" stop-opacity="0"/>
        </linearGradient>
      </defs>
      <path d="M0 330 L1120 300 L1120 662 L0 662 Z" fill="url(#darkPanel)"/>
      <rect x="0" y="286" width="236" height="10" fill="var(--stripe-blue)"/>
      <rect x="0" y="298" width="236" height="4" fill="var(--stripe-dark)"/>
      <rect x="700" y="262" width="420" height="10" fill="var(--stripe-blue)"/>
      <rect x="700" y="274" width="420" height="4" fill="var(--stripe-dark)"/>
      <circle cx="440" cy="104" r="92" fill="var(--navy)"/>
      <rect x="960" y="300" width="160" height="240" fill="url(#satelliteTone)" role="img" aria-label="Satellite illustration"/>
      <line x1="60" y1="566" x2="1060" y2="558" stroke="var(--rule)" stroke-width="2"/>
    </svg>

    <div class="brand">
      <span class="brand-lead">The</span>
      <span class="brand-name">Meridale Works</span>
    </div>

    <p class="tagline">Buy. Sell. Repair. Trade-in. New &amp; Used. All makes and models.</p>

    <p class="names">Dana &amp; Corin Halvik</p>

    <div class="contact-row primary">
      <span class="contact-item">
        <svg class="contact-icon" viewBox="0 0 30 30" aria-hidden="true">
          <circle cx="15" cy="15" r="14" fill="var(--icon-disc)"/>
          <path d="M10 8 l3 0 l1.5 4 l-2 1.5 q1.5 3 4 4.5 l1.5 -2 l4 1.5 l0 3 q-1 1.5 -3 1.5 q-9 -1 -10.5 -10.5 q0 -2 1.5 -3.5 z" fill="#0d1a4a"/>
        </svg>
        (555) 010-4821
      </span>
      <span class="contact-item">
        <svg class="contact-icon" viewBox="0 0 30 30" aria-hidden="true">
          <circle cx="15" cy="15" r="14" fill="var(--icon-disc)"/>
          <rect x="8" y="10" width="14" height="10" fill="none" stroke="#0d1a4a" stroke-width="2"/>
          <path d="M8 10 L15 16 L22 10" fill="none" stroke="#0d1a4a" stroke-width="2"/>
        </svg>
        corin@themeridaleworks.example
      </span>
    </div>

    <div class="contact-row secondary">
      <span class="contact-item">
        <svg class="contact-icon" viewBox="0 0 30 30" aria-hidden="true">
          <circle cx="15" cy="15" r="14" fill="var(--icon-disc)"/>
          <rect x="8" y="10" width="14" height="10" fill="none" stroke="#0d1a4a" stroke-width="2"/>
          <path d="M8 10 L15 16 L22 10" fill="none" stroke="#0d1a4a" stroke-width="2"/>
        </svg>
        dana@themeridaleworks.example
      </span>
    </div>
  </div>
</body>
</html>
```